Brindle Children's Center - Child Care brochure

I just bought a new child care and completely renovated the space. We are also designing a new website, so I need the brochure to match that with updated info. www.brindlechildrenscenter.com - Information on there is current. We expect to have the new one up and running in the next few days. We have new photo's that I'd like to be added to the flyer too. ps. the boys in the pictures are mine, so i would appreciate one of them being added :). support@pixelhutnetworks.com has details on the website (dev.brindlechildrenscenter.com). The child care program is only open during the ski season - i.e. a resort facility catering to high end clients.
I'm attaching the the website information, the flyer I created, logo files and pictures.

Target Market(s)

Parents of young children

Font styles to use
Other font styles liked:
• "Things we said" & "Calibri Light"

Colors
cfeae6
fef1ee

Requirements
Must have
• Pictures of children. sleek design - winter, mountain theme. Check with website designer on new website.
Nice to have
• prices included
Should not have
• Kid like artwork

```html
<!DOCTYPE html>
<html lang="en">
<head>
<meta charset="utf-8">
<title>Brindle Children's Center – Tri-fold Brochure</title>
<link href="https://fonts.googleapis.com/css2?family=Montserrat:wght@400;600;700&family=Open+Sans:wght@300;400;600&family=Dancing+Script:wght@500&display=swap" rel="stylesheet">
<style>
:root{
  --bg:#e6eff0;
  --teal:#9fd3cf;
  --teal-deep:#6fb8b3;
  --mint:#cfeae6;
  --blush:#fef1ee;
  --ink:#2c3b3b;
  --white:#ffffff;
  --photo-a:#b9a08a;
  --photo-b:#6d7d8f;
  --snow-a:#e8eef3;
  --snow-b:#8796a6;
}
*{box-sizing:border-box;margin:0;padding:0}
html,body{width:1200px;height:1000px;overflow:hidden}
body{background:var(--bg);font-family:"Open Sans",Arial,sans-serif;color:var(--ink);position:relative}
.spread{position:absolute;left:45px;width:1110px;height:450px;box-shadow:0 8px 22px rgba(0,0,0,.15);background:var(--blush);overflow:hidden}
.spread--outside{top:28px}
.spread--inside{top:522px}
.fold{position:absolute;top:0;width:1px;height:450px;background:rgba(0,0,0,.08)}
.photo{position:absolute}
.photo--classroom{background:linear-gradient(135deg,var(--photo-a) 0%,#d9c3b0 35%,#8fb5c8 65%,var(--photo-b) 100%)}
.photo--snow{background:linear-gradient(160deg,var(--snow-a) 0%,#c5d2dd 50%,var(--snow-b) 100%)}
.heading{font-family:"Montserrat",Arial,sans-serif;font-weight:700;text-transform:uppercase;letter-spacing:.5px}
.body-copy{font-weight:300;font-size:8.5px;line-height:1.5}
.script{font-family:"Dancing Script",cursive;font-weight:500}

/* prices */
.prices{position:absolute;left:0;top:0;width:370px;height:235px;background:var(--white)}
.prices__tag{position:absolute;left:20px;top:14px;height:30px;padding:0 16px 0 34px;background:var(--teal);color:var(--white);font-size:20px;line-height:30px}
.prices__tag::before{content:"$";position:absolute;left:9px;top:7px;width:16px;height:16px;border-radius:50%;background:var(--white);color:var(--teal-deep);font-size:10px;line-height:16px;text-align:center}
.rate{position:absolute;text-align:center}
.rate__name{display:inline-block;border:1px solid var(--teal);color:var(--teal-deep);font-size:19px;padding:0 8px}
.rate__time{font-size:7.5px;margin-top:4px}
.rate__price{display:inline-block;margin-top:4px;border:1px solid var(--teal);color:var(--teal-deep);font-family:"Montserrat",sans-serif;font-weight:600;font-size:10px;padding:2px 7px}
.prices__note{position:absolute;left:26px;top:176px;width:318px;text-align:center}
.prices__saving{font-family:"Montserrat",sans-serif;font-weight:700;font-size:8px;margin-top:4px}

.ski{position:absolute;left:0;top:235px;width:370px;height:215px;background:var(--teal);color:var(--white)}
.ski__title{position:absolute;left:22px;top:14px;font-size:14px}
.ski__sub{position:absolute;left:22px;top:32px;font-size:11px}
.ski__copy{position:absolute;left:22px;top:50px;width:185px;color:var(--ink)}
.diamond{position:absolute;width:48px;height:48px;background:var(--white);transform:rotate(45deg)}
.diamond span{position:absolute;inset:0;display:flex;flex-direction:column;align-items:center;justify-content:center;transform:rotate(-45deg);color:var(--teal-deep);font-family:"Montserrat",sans-serif;font-weight:700;font-size:10px}
.diamond small{font-family:"Open Sans",sans-serif;font-weight:300;font-size:6px}
.ski__evening{position:absolute;left:22px;bottom:12px;width:326px;height:32px;background:var(--white);color:var(--ink);font-size:7px;font-weight:600;padding:5px 10px;line-height:1.4}
.ski__evening b{position:absolute;right:10px;top:8px;border:1px solid var(--teal);color:var(--teal-deep);padding:1px 6px;font-family:"Montserrat",sans-serif;font-size:9px}

/* mission */
.mission{position:absolute;left:370px;top:215px;width:330px;height:235px;background:var(--blush)}
.mission__head{position:absolute;left:0;top:0;width:330px;height:62px;background:var(--teal)}
.mission__title{position:absolute;left:20px;top:12px;color:var(--white);line-height:1}
.mission__title .small{display:block;font-size:11px;font-weight:600;color:var(--ink)}
.mission__title .big{font-size:22px}
.mission__copy{position:absolute;left:20px;top:80px;width:290px;font-size:9.5px}

/* cover */
.cover__url{position:absolute;left:740px;top:14px;width:370px;height:24px;background:var(--teal);color:var(--white);font-size:10px;letter-spacing:1px;line-height:24px;padding-left:24px}
.cover__brand{position:absolute;left:740px;top:340px;width:340px;height:110px;background:var(--teal);padding:18px 22px}
.brand{display:flex;align-items:center;gap:10px}
.brand__dot{width:26px;height:26px;border-radius:50%;background:var(--white);flex:none}
.brand__name{font-family:"Montserrat",sans-serif;font-weight:700;font-size:13px;color:var(--ink);line-height:1.1;text-transform:uppercase}
.cover__contact{margin-top:10px;font-size:8px;line-height:1.55;color:var(--ink)}
.cover__edge{position:absolute;left:1080px;top:340px;width:30px;height:110px;background:var(--white)}

/* program */
.program__head{position:absolute;left:22px;top:16px;display:flex;align-items:center;gap:10px}
.program__head svg{flex:none}
.stack-title .small{display:block;font-size:12px;font-weight:600;color:var(--ink)}
.stack-title .big{display:block;font-size:22px;color:var(--teal-deep);line-height:1}
.steps{position:absolute;left:0;top:70px;width:70px;height:250px;background:var(--teal)}
.step{height:50px;padding:8px 0 0 12px;color:var(--white)}
.step b{display:block;font-family:"Montserrat",sans-serif;font-size:17px;line-height:1}
.step small{display:block;margin-top:4px;font-size:6.5px;font-weight:600;text-transform:uppercase;white-space:nowrap}
.program__copy{position:absolute;left:84px;top:74px;width:268px}
.program__copy p+p{margin-top:6px}

.staff__head{position:absolute;left:380px;top:30px;width:300px;height:58px;background:var(--teal);padding:6px 0 0 100px}
.staff__copy{position:absolute;left:392px;top:102px;width:320px}
.staff__copy p+p{margin-top:6px}
.your-photo{position:absolute;left:392px;top:220px;width:78px;height:78px;border-radius:50%;background:var(--white);border:3px solid var(--teal);display:flex;align-items:center;justify-content:center;text-align:center;font-family:"Montserrat",sans-serif;font-size:9px;color:var(--teal-deep);font-weight:600}
.staff__caption{position:absolute;left:484px;top:236px;width:200px;font-size:8px}

.services{position:absolute;left:740px;top:0;width:370px;height:450px;background:var(--blush)}
.services__top{position:absolute;left:0;top:40px;width:340px;height:180px;background:var(--teal)}
.services__title{position:absolute;left:92px;top:12px}
.services__title .small{color:var(--ink)}
.services__title .big{color:var(--white)}
.services__copy{position:absolute;left:92px;top:66px;width:228px;color:var(--ink)}
.services__box{position:absolute;left:92px;top:236px;width:250px}
.services__box h3{font-size:11px;color:var(--teal-deep);margin:8px 0 3px}
.services__photo{position:absolute;left:0;top:230px;width:80px;height:220px}
</style>
</head>
<body>

<section class="spread spread--outside" aria-label="Brochure outside">
  <div class="photo photo--classroom" style="left:370px;top:0;width:740px;height:450px" role="img" aria-label="Photo of children playing with puzzles at a classroom table"></div>

  <div class="prices">
    <div class="prices__tag heading">Prices</div>
    <div class="rate" style="left:22px;top:58px;width:150px">
      <div class="rate__name script">Full day</div>
      <div class="rate__time">(8:30 AM - 4:30 PM)</div>
      <div class="rate__price">$110</div>
    </div>
    <div class="rate" style="left:196px;top:58px;width:150px">
      <div class="rate__name script">Half day</div>
      <div class="rate__time">(8:30 AM - 12:30 PM)<br>(12:30 AM - 4:30 PM)</div>
      <div class="rate__price">$80</div>
    </div>
    <div class="rate" style="left:110px;top:122px;width:150px">
      <div class="rate__name script">5 day packages</div>
      <div class="rate__price">$500</div>
    </div>
    <div class="prices__note">
      <p class="body-copy">5-day packages can be used for any 5 days throughout the season. Unused days cannot be transferred to the next season. Reservations are required to use days from your package.</p>
      <p class="prices__saving">THAT'S A $50 SAVING!</p>
    </div>
  </div>

  <div class="ski">
    <h2 class="ski__title heading">New Season Ski</h2>
    <p class="ski__sub">Pass child care package</p>
    <p class="ski__copy body-copy">Verification of a season ski pass is required to receive the season ski pass child care package. Simply choose the package that best fits your needs, and visit our front desk to receive your child care card and enrollment paperwork.</p>
    <div class="diamond" style="left:248px;top:56px"><span>$900<small>10 days</small></span></div>
    <div class="diamond" style="left:228px;top:112px"><span>$1,800<small>20 days</small></span></div>
    <div class="diamond" style="left:300px;top:98px"><span>$2,700<small>30 days</small></span></div>
    <div class="diamond" style="left:300px;top:30px"><span>$3,600<small>40 days</small></span></div>
    <div class="ski__evening">FRIDAY AND SATURDAY ONLY<br>(4:30 PM - 9:00 PM)<b>$60</b></div>
  </div>

  <div class="mission">
    <div class="mission__head">
      <h2 class="mission__title heading"><span class="small">Our</span><span class="big">Mission</span></h2>
    </div>
    <p class="mission__copy body-copy">When you hit the slopes you want to know your children are in great hands. At our center, caring teachers create a warm, safe and playful space where little ones learn, rest and explore. Our goal is simple: give every family peace of mind and every child a mountain day full of friendship, discovery and fun, from the first run to the last lift.</p>
  </div>

  <div class="cover__url">www.brindlechildrenscenter.com</div>
  <div class="cover__brand">
    <div class="brand">
      <span class="brand__dot"></span>
      <span class="brand__name">Brindle<br>Children's Center</span>
    </div>
    <p class="cover__contact">4410 Summit Pass Road, Brindle, UT 84000<br>801.555.0142<br>hello@brindlechildrenscenter.com</p>
  </div>
  <div class="cover__edge"></div>

  <span class="fold" style="left:370px"></span><span class="fold" style="left:740px"></span>
</section>

<section class="spread spread--inside" aria-label="Brochure inside">
  <div class="program__head">
    <svg width="40" height="40" viewBox="0 0 40 40" aria-hidden="true">
      <g fill="var(--teal)">
        <circle cx="20" cy="20" r="12"/>
        <rect x="17" y="2" width="6" height="36"/>
        <rect x="2" y="17" width="36" height="6"/>
        <rect x="17" y="2" width="6" height="36" transform="rotate(45 20 20)"/>
        <rect x="17" y="2" width="6" height="36" transform="rotate(-45 20 20)"/>
      </g>
      <circle cx="20" cy="20" r="5" fill="var(--blush)"/>
    </svg>
    <h2 class="stack-title heading"><span class="small">Our</span><span class="big">Program</span></h2>
  </div>
  <div class="steps">
    <div class="step"><b>01</b><small>Arrival</small></div>
    <div class="step"><b>02</b><small>Free play</small></div>
    <div class="step"><b>03</b><small>Snow time</small></div>
    <div class="step"><b>04</b><small>Lunch &amp; rest</small></div>
    <div class="step"><b>05</b><small>Story time</small></div>
  </div>
  <div class="program__copy body-copy">
    <p>Our daily program is built around the rhythm of a mountain day. Children are welcomed by their teachers, settle in with a calm morning activity and choose from puzzles, blocks and reading corners.</p>
    <p>Free play encourages sharing, imagination and confidence, with teachers guiding small groups through hands-on activities suited to each age.</p>
    <p>When the weather allows, we head outside to play in the snow, build, slide and explore the fresh air safely together.</p>
    <p>A healthy lunch is followed by quiet rest time, so every child recharges for the afternoon ahead.</p>
    <p>We end the day with crafts, music and stories until parents return from the slopes.</p>
  </div>
  <div class="photo photo--snow" style="left:0;top:330px;width:150px;height:120px" role="img" aria-label="Photo of the snowy resort village"></div>
  <div class="photo photo--snow" style="left:154px;top:330px;width:216px;height:120px" role="img" aria-label="Photo of snow-covered mountain slopes"></div>

  <div class="staff__head"><h2 class="stack-title heading"><span class="small">Our</span><span class="big" style="color:var(--white)">Staff</span></h2></div>
  <div class="staff__copy body-copy">
    <p>At our center, every teacher is trained in early childhood care, first aid and CPR. Our team loves the mountains as much as the children do, and brings patience, warmth and energy to every day.</p>
    <p>Small group sizes mean each child receives personal attention, and families always know who is caring for their little ones.</p>
  </div>
  <div class="your-photo">YOUR<br>PHOTO</div>
  <p class="staff__caption body-copy">My name is Jane, director of our center. I look forward to meeting you and your family this season.</p>
  <div class="photo photo--snow" style="left:370px;top:330px;width:370px;height:120px" role="img" aria-label="Photo of a snowy mountain lodge"></div>

  <div class="services">
    <div class="services__top">
      <h2 class="services__title stack-title heading"><span class="small">Our</span><span class="big">Services</span></h2>
      <p class="services__copy body-copy">Our center is a full-service, licensed child care facility for children ages two through eight. We offer full and half day care throughout the ski season, plus evening care on weekends, so parents can enjoy every run.</p>
    </div>
    <div class="services__box">
      <h3 class="heading">Registration</h3>
      <p class="body-copy">We highly recommend making advance reservations, as space is limited each day. Forms can be completed at our front desk or online before arrival.</p>
      <h3 class="heading">Cancellation</h3>
      <p class="body-copy">Please cancel at least 24 hours before your reserved day. Late cancellations and no-shows will be charged the full daily rate.</p>
    </div>
    <div class="services__photo photo photo--snow" role="img" aria-label="Photo of snowy slopes and pine trees"></div>
  </div>

  <span class="fold" style="left:370px"></span><span class="fold" style="left:740px"></span>
</section>

</body>
</html>
```